Dynamic Business Card for Sports Supplements Company

Hi! I'm looking for an awesome business card to match my existing sports supplement company. I have uploaded my current company logo and screenshot of the front page of my website.

I would like to have something dynamic and interesting and utilize the colors in the website - the reds and purples

The business card should be double sided and focus on a unique eye-catching design on the back and include all the relevant company info.

Most importantly, it should say somewhere: "Sign up on our website for a coupon code."

Target Market(s)

Mostly for women gym goers but it shouldn't be too feminine. It should be in keeping with the website design. It should flow and clearly be connected to it

Industry/Entity Type

Business

Contact Information for Business Card

Lorena K. Vasquez
CEO
LVasquez@Fortivanco.example
www.fortivanco.example
614.275.3081
P.O. Box 48317
Burke, Virginia 22417

Sign up on our website for a coupon code

Font styles to use
Serif
Sans Serif
Other font styles liked:
• Novecento font family and "Fortivan" is in AR Destine font

Requirements
Must have
• One side should be a bold Fortivan logo design. Even just the symbol itself may be o.k. (see attached file)

```html
<!DOCTYPE html>
<html lang="en">
<head>
<meta charset="utf-8">
<title>Fortivan Business Card</title>
<link href="https://fonts.googleapis.com/css2?family=Open+Sans:wght@400;700&family=Lobster+Two:ital,wght@1,700&display=swap" rel="stylesheet">
<style>
  :root {
    --bg: #3a3c40;
    --red: #e8232a;
    --red-deep: #c8383f;
    --purple: #93309a;
    --purple-deep: #6b2a72;
    --silver-light: #e4e4e6;
    --silver-dark: #9c9ea3;
    --white: #ffffff;
  }
  * { box-sizing: border-box; margin: 0; padding: 0; }
  html, body { width: 1200px; height: 1000px; overflow: hidden; }
  body {
    background: var(--bg);
    font-family: "Open Sans", Arial, sans-serif;
    position: relative;
  }
  .card {
    position: absolute;
    width: 630px;
    height: 360px;
    overflow: hidden;
    box-shadow: 0 10px 24px rgba(0,0,0,.45);
  }

  /* Back side: bold brand side */
  .card-back { left: 500px; top: 70px; background: var(--purple); }
  .card-back .red-band {
    position: absolute; left: 0; top: 0; width: 100%; height: 108px;
    background: var(--red);
  }
  .card-back .silver-line {
    position: absolute; left: 0; top: 108px; width: 100%; height: 6px;
    background: linear-gradient(var(--silver-light), var(--silver-dark));
  }
  .card-back .coupon-note {
    position: absolute; right: 18px; top: 40px;
    font-size: 12px; color: var(--white); letter-spacing: .2px;
    white-space: nowrap;
  }
  .card-back .brand {
    position: absolute; left: 0; right: 0; top: 78px;
    display: flex; flex-direction: column; align-items: center;
  }
  .brand-mark {
    width: 64px; height: 64px;
    background: var(--silver-light);
  }
  .brand-name {
    margin-top: 14px;
    font-weight: 700; font-size: 44px; letter-spacing: 2px;
    color: var(--white); line-height: 1;
  }
  .brand-tagline {
    margin-top: 4px;
    font-size: 26px; color: var(--white); line-height: 1.1;
  }

  /* Front side: contact details */
  .card-front { left: 70px; top: 570px; background: var(--purple-deep); }
  .card-front .red-panel {
    position: absolute; left: 0; top: 0; width: 230px; height: 100%;
    background: linear-gradient(90deg, var(--red) 55%, var(--red-deep));
  }
  .card-front .silver-stripe {
    position: absolute; left: 230px; top: 0; width: 22px; height: 100%;
    background: linear-gradient(90deg, var(--silver-dark), var(--silver-light), var(--silver-dark));
  }
  .card-front .purple-panel {
    position: absolute; left: 252px; top: 0; right: 0; height: 100%;
    background: linear-gradient(135deg, var(--purple-deep), #7a3080);
  }
  .card-front .brand {
    position: absolute; left: 0; width: 230px; top: 95px;
    display: flex; flex-direction: column; align-items: center;
  }
  .card-front .brand-mark { width: 48px; height: 48px; background: var(--white); }
  .card-front .brand-name { font-size: 30px; margin-top: 12px; letter-spacing: 1px; }
  .card-front .brand-tagline { font-size: 17px; margin-top: 2px; }
  .person {
    position: absolute; right: 40px; top: 38px; text-align: right; color: var(--white);
  }
  .person-name {
    font-family: "Lobster Two", Georgia, serif; font-style: italic; font-weight: 700;
    font-size: 34px; padding: 0 6px 4px 20px;
    border-bottom: 2px solid var(--white); display: inline-block; line-height: 1.1;
  }
  .person-title {
    font-family: "Lobster Two", Georgia, serif; font-style: italic; font-size: 18px;
    margin-top: 6px;
  }
  .contact {
    position: absolute; left: 282px; bottom: 34px; color: var(--white);
    font-size: 19px; line-height: 1.45;
  }
</style>
</head>
<body>

  <section class="card card-back" aria-label="Card back">
    <div class="red-band"></div>
    <div class="silver-line"></div>
    <p class="coupon-note">Sign up on our website for a coupon code &gt;&gt;</p>
    <div class="brand">
      <div class="brand-mark"></div>
      <div class="brand-name">FORTIVAN</div>
      <div class="brand-tagline">your strength source</div>
    </div>
  </section>

  <section class="card card-front" aria-label="Card front">
    <div class="red-panel"></div>
    <div class="silver-stripe"></div>
    <div class="purple-panel"></div>
    <div class="brand">
      <div class="brand-mark"></div>
      <div class="brand-name">FORTIVAN</div>
      <div class="brand-tagline">your strength source</div>
    </div>
    <div class="person">
      <div class="person-name">Lorena K.</div>
      <div class="person-title">CEO</div>
    </div>
    <div class="contact">
      <div class="contact-email">LVasquez@Fortivanco.example</div>
      <div class="contact-web">www.fortivanco.example</div>
    </div>
  </section>

</body>
</html>
```